Velmora Datatech Solutions- Computer Network Company

Wordpress designs.

I want a web design that is up scale looking, high-end. A very modern and clean looking.

Thinking of rotating pictures of Network Management (picture of server/desktop computer), Backup Solutions (picture of server after fire), Network wiring (picture maybe of racks/switches, etc)

Service- Backup Solutions, Managing computers and servers, Database management, Network Wiring, Phone system management

Products we sell Tovo computers, KX printers,
About the company
Contact us

Target Market(s)

Companies looking for Computer support, Law office, Private business

Industry/Entity Type

Computer

Coding

Coded - Design and coding required

Font styles to use
Sans Serif

Requirements
Must have
• Wordpress design, will be hosted on a Linux server.
• Use the logo in the design, Clean, Up scale website
• Navigation- Services-Products -About Us-Contact Us
• ***Also, a link for Buying a domain (we are a reseller of hosting and domain names)*****
Nice to have
• picture rotation on the landing page, Network Management,

```html
<!DOCTYPE html>
<html lang="en">
<head>
<meta charset="utf-8">
<title>Velmora Datatech Solutions</title>
<link href="https://fonts.googleapis.com/css2?family=Open+Sans:wght@400;600;700&family=Roboto:wght@400;500;700&display=swap" rel="stylesheet">
<style>
:root{
  --blue:#1f3f8f;
  --blue-bright:#2f5fd0;
  --green:#0f7a45;
  --green-dark:#0d4f32;
  --dark:#2b2b2b;
  --darker:#1b1b1b;
  --grey:#ededed;
  --text:#333;
  --white:#fff;
}
*{margin:0;padding:0;box-sizing:border-box}
html,body{width:1200px;height:3255px;overflow:hidden}
body{font-family:"Open Sans",sans-serif;color:var(--text);background:var(--white);position:relative}
.abs{position:absolute}
h1,h2,h3,.heading{font-family:"Roboto",sans-serif;font-weight:500}

/* header */
.header{left:0;top:0;width:1200px;height:130px;background:linear-gradient(#fff,#f1f3f6);border-bottom:1px solid #d9dde3}
.topbar{right:0;top:0;height:40px;width:354px;background:var(--green-dark);border-radius:0 0 0 6px}
.topbar .phone{left:44px;top:10px;color:#fff;font-size:16px}
.social-dot{width:30px;height:30px;border:2px solid #222;border-radius:50%;background:#fff;top:5px}
.brand{left:60px;top:38px;font-family:"Roboto",sans-serif;font-weight:700;font-size:34px;color:var(--blue);display:flex;align-items:center;gap:12px}
.brand .mark{width:22px;height:22px;border-radius:50%;background:var(--green)}
.nav{right:60px;top:70px;display:flex;gap:4px;font-family:"Roboto",sans-serif;font-weight:500;font-size:15px}
.nav a{color:#222;text-decoration:none;padding:10px 14px}
.nav a.active{background:var(--blue);color:#fff}

/* hero */
.hero{left:0;top:130px;width:1200px;height:570px;background:linear-gradient(135deg,#9fd4f0 0%,#3f9fd6 45%,#1b6aa8 100%)}
.hero-tag{font-family:"Roboto",sans-serif;font-size:36px;color:#fff;padding:10px 24px;letter-spacing:.5px}
.tag-blue{left:248px;top:370px;background:rgba(31,63,143,.9)}
.tag-green{left:262px;top:443px;background:rgba(15,122,69,.9)}
.arrow-btn{width:34px;height:60px;background:#fff;top:375px;display:flex;align-items:center;justify-content:center}

/* welcome */
.welcome-title{left:0;top:770px;width:1200px;text-align:center;font-size:44px;color:#111}
.welcome-title span{color:var(--blue);font-weight:700}
.welcome-text{left:170px;top:878px;width:860px;text-align:center;font-size:14.5px;line-height:26px;color:#555}
.btn{font-family:"Open Sans",sans-serif;font-weight:600;color:#fff;font-size:17px;text-align:center}
.btn-contact{left:506px;top:1020px;width:182px;height:46px;line-height:46px;background:var(--blue);border-radius:3px}

/* services */
.services{left:0;top:1146px;width:1200px;height:681px;background:radial-gradient(ellipse at 60% 45%,#3a3f47 0%,#1d1f23 60%,#121316 100%)}
.services-title{left:0;top:1222px;width:1200px;text-align:center;color:#fff;font-size:40px}
.svc{color:#fff;width:270px}
.svc h3{font-size:20px;font-weight:400;margin-bottom:8px}
.svc p{font-size:12.5px;line-height:18px}
.svc.left{text-align:center}

/* reseller */
.reseller{left:0;top:1827px;width:620px;height:376px;background:var(--grey)}
.reseller h2{left:64px;top:1878px;font-size:34px;font-weight:400;color:#111}
.reseller h2 span{color:var(--blue-bright);font-weight:500}
.rule{left:64px;top:1928px;width:265px;height:2px;background:#999}
.reseller h4{left:64px;top:1950px;font-size:16px;font-weight:700;color:#222}
.reseller-text{left:64px;top:1982px;width:510px;font-size:13.5px;line-height:23px;color:#666}
.btn-domain{left:60px;top:2092px;width:220px;height:46px;line-height:46px;background:var(--green-dark);font-size:16px}
.support{left:620px;top:1827px;width:580px;height:376px;background:var(--blue)}
.support h2{left:680px;top:1875px;color:#fff;font-size:28px;font-weight:400}
.support p{left:680px;top:1917px;width:440px;color:#fff;font-size:14.5px;line-height:20px}
.field{left:680px;width:410px;height:40px;background:#fff;border-radius:2px;font-size:13px;color:#999;padding:11px 14px}
.btn-submit{left:682px;top:2120px;width:166px;height:46px;line-height:46px;background:#fff;color:#111;font-size:16px;border-radius:3px}

/* products */
.products-title{left:0;top:2262px;width:1200px;text-align:center;font-size:44px;color:#111}
.product{top:2387px;width:321px;height:308px}
.product .photo{left:0;top:0;width:321px;height:245px}
.product .band{left:0;top:245px;width:321px;height:63px;background:var(--blue)}
.product .name{left:14px;top:263px;color:#fff;font-family:"Roboto",sans-serif;font-size:26px;font-weight:500}
.product .buy{right:14px;top:256px;width:96px;height:42px;line-height:42px;background:#fff;color:#111;text-align:center;font-size:16px}

/* cta */
.cta{left:0;top:2788px;width:1200px;height:135px;background:var(--green);color:#fff;text-align:center}
.cta h2{position:absolute;left:0;top:30px;width:1200px;font-size:28px;font-weight:500}
.cta p{position:absolute;left:0;top:80px;width:1200px;font-size:24px;display:flex;justify-content:center;align-items:center;gap:10px}

/* footer */
.footer{left:0;top:2923px;width:1200px;height:289px;background:var(--dark);color:#fff}
.footer-brand{left:60px;top:3060px;font-family:"Roboto",sans-serif;font-weight:700;font-size:34px;color:#fff;display:flex;align-items:center;gap:12px}
.footer-brand .mark{width:22px;height:22px;border-radius:50%;background:#fff}
.footer h3{font-size:22px;font-weight:400;color:#fff}
.f-input{left:425px;width:218px;background:#fff;font-size:13px;color:#888;padding:6px 8px}
.btn-send{left:555px;top:3130px;width:85px;height:38px;line-height:38px;background:var(--blue-bright);font-size:16px;border-radius:2px}
.links{left:716px;top:3010px;list-style:none;font-size:12.5px;line-height:28px}
.links li::before{content:"";display:inline-block;width:5px;height:5px;border-radius:50%;background:var(--blue-bright);margin-right:10px;vertical-align:middle}
.contact-list{left:920px;top:3010px;font-size:13px;line-height:31px}
.contact-list div{display:flex;align-items:center;gap:14px}
.f-social{top:3114px;width:26px;height:26px;border-radius:50%;background:#ddd}
.copyright{left:0;top:3212px;width:1200px;height:43px;background:var(--darker);color:#ddd;font-size:12px;text-align:center;line-height:43px}
</style>
</head>
<body>

<!-- header -->
<header class="abs header"></header>
<div class="abs topbar">
  <svg class="abs" style="left:16px;top:11px" width="18" height="18" viewBox="0 0 24 24"><path fill="#fff" d="M6.6 10.8a15 15 0 0 0 6.6 6.6l2.2-2.2a1 1 0 0 1 1-.25 11.4 11.4 0 0 0 3.6.57 1 1 0 0 1 1 1V20a1 1 0 0 1-1 1A17 17 0 0 1 3 4a1 1 0 0 1 1-1h3.5a1 1 0 0 1 1 1c0 1.25.2 2.45.57 3.57a1 1 0 0 1-.25 1z"/></svg>
  <div class="abs phone">877-555-0142</div>
  <div class="abs social-dot" style="left:236px"></div>
  <div class="abs social-dot" style="left:272px"></div>
  <div class="abs social-dot" style="left:308px"></div>
</div>
<div class="abs brand"><span class="mark"></span>Velmora</div>
<nav class="abs nav">
  <a class="active">HOME</a><a>SERVICES</a><a>PRODUCTS</a><a>ABOUT US</a><a>BUY A DOMAIN</a><a>CONTACT US</a>
</nav>

<!-- hero -->
<section class="abs hero" role="img" aria-label="Rotating photo of networked laptops around a glass globe"></section>
<div class="abs hero-tag tag-blue">A PLACE OF YOUR COMPLETE SOLUTIONS</div>
<div class="abs hero-tag tag-green">WE FULLFILLS ALL TECHNOLOGY NEEDS</div>
<div class="abs arrow-btn" style="left:0"><svg width="14" height="22" viewBox="0 0 14 22"><path d="M12 2 3 11l9 9" fill="none" stroke="#222" stroke-width="3"/></svg></div>
<div class="abs arrow-btn" style="right:0"><svg width="14" height="22" viewBox="0 0 14 22"><path d="M2 2l9 9-9 9" fill="none" stroke="#222" stroke-width="3"/></svg></div>

<!-- welcome -->
<h1 class="abs welcome-title">Welcome to <span>Velmora</span></h1>
<p class="abs welcome-text">Lorem Ipsum is simply dummy text of the printing and typesetting industry. Lorem Ipsum has been the industry's standard dummy text ever since the 1500s, when an unknown printer took a galley of type and scrambled it to make a type specimen book. It has survived not only five centuries, but also the leap into electronic typesetting, remaining essentially unchanged. It was popularised in the 1960s with the release of Lettrex sheets containing.</p>
<div class="abs btn btn-contact">Contact us Today</div>

<!-- services -->
<section class="abs services" role="img" aria-label="Dark background photo of business people network"></section>
<h2 class="abs services-title">Services we provide</h2>
<svg class="abs" style="left:0;top:1146px" width="1200" height="681" viewBox="0 1146 1200 681">
  <g stroke="#fff" stroke-width="1.5" fill="#fff">
    <line x1="290" y1="1415" x2="385" y2="1415"/><path d="M292 1411l-7 4 7 4z"/>
    <line x1="770" y1="1415" x2="860" y2="1415"/><path d="M858 1411l7 4-7 4z"/>
    <line x1="250" y1="1540" x2="346" y2="1540"/><path d="M252 1536l-7 4 7 4z"/>
    <line x1="815" y1="1540" x2="880" y2="1540"/><path d="M878 1536l7 4-7 4z"/>
    <line x1="305" y1="1680" x2="391" y2="1680"/><path d="M307 1676l-7 4 7 4z"/>
    <line x1="750" y1="1680" x2="840" y2="1680"/><path d="M838 1676l7 4-7 4z"/>
  </g>
  <circle cx="597" cy="1536" r="178" fill="#fff"/>
  <g fill="var(--blue-bright)" stroke="#fff" stroke-width="4">
    <circle cx="445" cy="1415" r="60"/><circle cx="710" cy="1415" r="60"/>
    <circle cx="406" cy="1540" r="60"/><circle cx="755" cy="1540" r="60"/>
    <circle cx="451" cy="1680" r="60"/><circle cx="690" cy="1680" r="60"/>
  </g>
  <!-- cloud upload -->
  <path d="M420 1432h50a14 14 0 0 0 0-28 20 20 0 0 0-38-4 14 14 0 0 0-12 32z" fill="#fff"/>
  <path d="M445 1428v-20m-8 8 8-8 8 8" stroke="var(--blue-bright)" stroke-width="4" fill="none"/>
  <!-- share -->
  <g fill="#fff"><circle cx="696" cy="1415" r="8"/><circle cx="724" cy="1400" r="8"/><circle cx="724" cy="1430" r="8"/></g>
  <path d="M696 1415l28-15M696 1415l28 15" stroke="#fff" stroke-width="4"/>
  <!-- monitor -->
  <rect x="382" y="1521" width="48" height="32" rx="2" fill="none" stroke="#fff" stroke-width="4"/>
  <path d="M406 1553v8M394 1562h24" stroke="#fff" stroke-width="4"/>
  <!-- phone -->
  <path d="M740 1524a4 4 0 0 1 5-1l6 8a3 3 0 0 1-1 4l-3 3a22 22 0 0 0 10 10l3-3a3 3 0 0 1 4-1l8 6a4 4 0 0 1 1 5l-4 4c-14 0-34-20-34-34z" fill="#fff"/>
  <g fill="#fff"><circle cx="768" cy="1535" r="2.5"/><circle cx="775" cy="1535" r="2.5"/><circle cx="782" cy="1535" r="2.5"/></g>
  <!-- database search -->
  <ellipse cx="445" cy="1664" rx="18" ry="7" fill="#fff"/>
  <path d="M427 1664v28c0 4 8 7 18 7s18-3 18-7v-28" fill="none" stroke="#fff" stroke-width="4"/>
  <circle cx="460" cy="1690" r="9" fill="var(--blue-bright)" stroke="#fff" stroke-width="4"/>
  <path d="M466 1696l8 8" stroke="#fff" stroke-width="4"/>
  <!-- server -->
  <g fill="#fff"><rect x="668" y="1660" width="44" height="11"/><rect x="668" y="1675" width="44" height="11"/><rect x="668" y="1690" width="44" height="11"/></g>
  <g fill="var(--blue-bright)"><circle cx="675" cy="1665" r="2"/><circle cx="675" cy="1680" r="2"/><circle cx="675" cy="1695" r="2"/></g>
  <text x="597" y="1546" text-anchor="middle" font-family="Roboto, sans-serif" font-weight="700" font-size="36" fill="#1f3f8f">Velmora</text>
</svg>
<div class="abs svc left" style="left:36px;top:1395px"><h3>Backup Solutions</h3><p>She packed her seven versalia, put her into the belt and made on the way.</p></div>
<div class="abs svc" style="left:868px;top:1395px"><h3>Network Wiring</h3><p>She packed her seven versalia, put her into the belt and made on the way.</p></div>
<div class="abs svc left" style="left:14px;top:1520px"><h3>Managing computers</h3><p>She packed her seven versalia, put her into the belt and made on the way. When she reached the first .</p></div>
<div class="abs svc" style="left:890px;top:1520px;width:300px"><h3>Phone system management</h3><p style="width:270px">She packed her seven versalia, put her into the belt and made on the way.</p></div>
<div class="abs svc left" style="left:40px;top:1670px"><h3>Database management</h3><p>She packed her seven versalia, put her into the belt and made on the way.</p></div>
<div class="abs svc" style="left:860px;top:1665px"><h3>Servers</h3><p>She packed her seven versalia, put her into the belt and made on the way. When she reached the first .</p></div>

<!-- reseller + support -->
<section class="abs reseller"></section>
<h2 class="abs reseller heading" style="position:absolute;left:64px;top:1872px;font-size:34px;font-weight:400;color:#111">We are a reseller with <span style="color:var(--blue-bright);font-weight:500">Domainora</span></h2>
<div class="abs rule"></div>
<h4 class="abs" style="left:64px;top:1950px;font-size:16px;font-weight:700;color:#222">Are you looking for a Domain with Domainora?</h4>
<p class="abs reseller-text">Lorem Ipsum is simply dummy text of the printing and typesetting industry. Lorem Ipsum has been the industry's standard dummy text ever since the 1500s, when an unknown printer took a galley of type and scrambled it to make a type specimen book. It has survived not only five centuries.</p>
<div class="abs btn btn-domain">Buying a Domain name</div>

<section class="abs support"></section>
<h2 class="abs" style="left:680px;top:1875px;color:#fff;font-size:28px;font-weight:400">Looking for Computer support?</h2>
<p class="abs" style="left:680px;top:1917px;width:440px;color:#fff;font-size:14.5px;line-height:20px">Contact with us Today we solve your all issue and provide you solutions</p>
<div class="abs field" style="top:1978px">Name</div>
<div class="abs field" style="top:2024px">Email</div>
<div class="abs field" style="top:2070px">Phone no</div>
<div class="abs btn btn-submit">Submit Query</div>

<!-- products -->
<h2 class="abs products-title">Products we sell</h2>
<div class="abs product" style="left:59px">
  <div class="abs photo" role="img" aria-label="Photo of a KX laser printer on a desk" style="background:linear-gradient(160deg,#8a7a6a,#2a2624 60%,#4a3a30)"></div>
  <div class="abs band"></div><div class="abs name">PRINTERS</div><div class="abs buy">Buy Now</div>
</div>
<div class="abs product" style="left:445px">
  <div class="abs photo" role="img" aria-label="Photo of a Tovo laptop on a wooden table" style="background:linear-gradient(160deg,#2a2a2a,#5a4a3a 55%,#8a6a48)"></div>
  <div class="abs band"></div><div class="abs name">LAPTOPS</div><div class="abs buy">Buy Now</div>
</div>
<div class="abs product" style="left:825px">
  <div class="abs photo" role="img" aria-label="Photo of a Tovo desktop computer in an office" style="background:linear-gradient(160deg,#c9ccd2,#e8ecef 50%,#7a8088)"></div>
  <div class="abs band"></div><div class="abs name">DESKTOPS</div><div class="abs buy">Buy Now</div>
</div>

<!-- call to action -->
<section class="abs cta">
  <h2>Reach out to us for Business, Query, Buy or sell computers and Support</h2>
  <p>Call us Today
    <svg width="34" height="34" viewBox="0 0 34 34"><circle cx="17" cy="17" r="15" fill="none" stroke="#fff" stroke-width="2"/><path d="M11 10a2 2 0 0 1 2-1l3 4a2 2 0 0 1-1 2l-1 1a10 10 0 0 0 5 5l1-1a2 2 0 0 1 2-1l4 3a2 2 0 0 1 0 2l-2 2c-7 0-14-7-14-14z" fill="#fff"/></svg>
    (212) 555 0190</p>
</section>

<!-- footer -->
<footer class="abs footer"></footer>
<div class="abs footer-brand"><span class="mark"></span>Velmora</div>
<h3 class="abs" style="left:425px;top:2968px;font-size:22px;font-weight:400;color:#fff">Query us</h3>
<div class="abs f-input" style="top:3018px;height:40px;padding-top:11px">Email</div>
<div class="abs f-input" style="top:3062px;height:58px">Your Message</div>
<div class="abs btn btn-send">Send</div>
<h3 class="abs" style="left:712px;top:2968px;font-size:22px;font-weight:400;color:#fff">Quick Links</h3>
<ul class="abs links" style="color:#fff">
  <li>About Us</li><li>Privacy Policy</li><li>Terms &amp; Condition</li><li>Best Seller</li><li>Manufactures</li>
</ul>
<h3 class="abs" style="left:918px;top:2968px;font-size:22px;font-weight:400;color:#fff">Contact us</h3>
<div class="abs contact-list" style="color:#fff">
  <div><svg width="18" height="18" viewBox="0 0 24 24"><path fill="#3a7be0" d="M6.6 10.8a15 15 0 0 0 6.6 6.6l2.2-2.2a1 1 0 0 1 1-.25 11.4 11.4 0 0 0 3.6.57 1 1 0 0 1 1 1V20a1 1 0 0 1-1 1A17 17 0 0 1 3 4a1 1 0 0 1 1-1h3.5a1 1 0 0 1 1 1c0 1.25.2 2.45.57 3.57a1 1 0 0 1-.25 1z"/></svg>Phone: 877-555-0142</div>
  <div><svg width="18" height="18" viewBox="0 0 24 24"><rect x="6" y="3" width="12" height="6" fill="#3a7be0"/><rect x="3" y="9" width="18" height="9" rx="2" fill="#3a7be0"/><rect x="7" y="14" width="10" height="7" fill="#fff" stroke="#3a7be0" stroke-width="2"/></svg>Fax: 609-555-0187</div>
  <div><svg width="18" height="18" viewBox="0 0 24 24"><rect x="2" y="5" width="20" height="14" fill="#3a7be0"/><path d="M2 5l10 8 10-8" fill="none" stroke="#fff" stroke-width="2"/></svg>Email: info@velmoradata.com</div>
</div>
<div class="abs f-social" style="left:924px"></div>
<div class="abs f-social" style="left:954px"></div>
<div class="abs f-social" style="left:984px"></div>
<div class="abs f-social" style="left:1014px"></div>
<div class="abs f-social" style="left:1044px"></div>
<div class="abs copyright">©2016 VELMORA ALL RIGHT RESERVED</div>

</body>
</html>
```